Business Card for a Floral & Decorating Business

I would like to take my current logo and create a better business card. I am looking for elegance as I am a florist and event decorator. My logo has multiple colour options. I like colours like green, purple, pink and orange, I think I would like a white card, open to black back ground. I want it to feel elegant and romantic. I like metallic lettering that maybe is indented in the paper, I also like glossy paper. I have a full logo already as well as a badge. I have attached both in multiple colours.m
Updates

Need extra days to review

Target Market(s)

Weddings, special events, floral customers

Industry/Entity Type

Floral and decorating

Contact Information for Business Card

Phone number, email, instagram, facebook, title, name, logo

Font styles to use
Script

Requirements
Nice to have
• Elegant

```html
<!DOCTYPE html>
<html lang="en">
<head>
<meta charset="utf-8">
<title>Wren Halloway — Business Card</title>
<link rel="stylesheet" href="https://fonts.googleapis.com/css2?family=Open+Sans:wght@400;600&family=Cormorant+Garamond:wght@500&display=swap">
<style>
  :root {
    --backdrop: #b0b2b1;
    --card-white: #ffffff;
    --plum: #84678f;
    --ink: #2e2e30;
    --silver-soft: #ececee;
    --silver-mid: #d4d4d8;
    --silver-bright: #f6f6f8;
  }
  html, body {
    margin: 0;
    padding: 0;
    width: 1011px;
    height: 1200px;
    overflow: hidden;
    background: var(--backdrop);
  }
  .stage {
    position: relative;
    width: 1011px;
    height: 1200px;
    font-family: "Open Sans", Arial, sans-serif;
  }
  .card {
    position: absolute;
    left: 139px;
    width: 735px;
    height: 431px;
    overflow: hidden;
    box-shadow: 0 0 0 1px rgba(0,0,0,0.12), 0 2px 6px rgba(0,0,0,0.15);
  }
  .card--front { top: 123px; background: var(--card-white); }
  .card--back  { top: 646px; background: var(--plum); }

  .side-floral {
    position: absolute;
    top: 0;
    width: 122px;
    height: 100%;
  }
  .side-floral--left  { left: 0; }
  .side-floral--right { right: 0; }
  .card--front .side-floral--left  { background: linear-gradient(90deg, var(--silver-soft), rgba(255,255,255,0)); }
  .card--front .side-floral--right { background: linear-gradient(270deg, var(--silver-soft), rgba(255,255,255,0)); }
  .card--back .side-floral--left  { background: linear-gradient(90deg, var(--silver-mid), rgba(132,103,143,0)); opacity: 0.75; }
  .card--back .side-floral--right { background: linear-gradient(270deg, var(--silver-mid), rgba(132,103,143,0)); opacity: 0.75; }

  .brand {
    position: absolute;
    left: 0;
    right: 0;
    text-align: center;
  }
  .brand__mark {
    display: block;
    width: 60px;
    height: 60px;
    margin: 0 auto 22px;
    border: 2px solid currentColor;
    border-radius: 50%;
    box-sizing: border-box;
  }
  .brand__name {
    font-family: "Open Sans", Arial, sans-serif;
    font-weight: 400;
    font-size: 44px;
    line-height: 1;
    letter-spacing: 1px;
  }
  .brand__tagline {
    margin-top: 14px;
    font-family: "Cormorant Garamond", Georgia, serif;
    font-weight: 500;
    font-size: 13px;
    letter-spacing: 5px;
  }
  .card--front .brand { top: 50px; color: var(--plum); }
  .card--back  .brand { top: 124px; color: var(--card-white); }

  .contact {
    position: absolute;
    top: 290px;
    left: 0;
    right: 0;
    display: flex;
    justify-content: center;
  }
  .contact__person {
    text-align: right;
    padding-right: 18px;
    border-right: 1.5px solid var(--plum);
    padding-top: 4px;
    height: 62px;
  }
  .contact__name {
    font-weight: 600;
    font-size: 20px;
    color: var(--plum);
    line-height: 1.2;
  }
  .contact__title {
    font-size: 20px;
    color: var(--ink);
    margin-top: 6px;
    line-height: 1.2;
  }
  .contact__list {
    list-style: none;
    margin: 0;
    padding: 0 0 0 18px;
  }
  .contact__item {
    display: flex;
    align-items: center;
    font-size: 18px;
    color: var(--ink);
    height: 26px;
  }
  .contact__icon {
    width: 18px;
    height: 18px;
    margin-right: 10px;
    flex: none;
  }
  .services {
    position: absolute;
    top: 386px;
    left: 0;
    right: 0;
    text-align: center;
    font-size: 19px;
    color: var(--plum);
  }
</style>
</head>
<body>
<div class="stage">

  <section class="card card--front">
    <div class="side-floral side-floral--left" role="img" aria-label="Faint silver line-drawn flowers along the left edge"></div>
    <div class="side-floral side-floral--right" role="img" aria-label="Faint silver line-drawn flowers along the right edge"></div>

    <div class="brand">
      <span class="brand__mark"></span>
      <div class="brand__name">Wren Halloway</div>
      <div class="brand__tagline">DECORATING &amp; FLORALS.</div>
    </div>

    <div class="contact">
      <div class="contact__person">
        <div class="contact__name">Wren Halloway</div>
        <div class="contact__title">Owner</div>
      </div>
      <ul class="contact__list">
        <li class="contact__item">
          <svg class="contact__icon" viewBox="0 0 18 18" fill="none" stroke="#84678f" stroke-width="1.6">
            <rect x="5" y="2" width="8" height="14" rx="1.5"/>
            <line x1="8" y1="13.5" x2="10" y2="13.5"/>
          </svg>
          555 010 2387
        </li>
        <li class="contact__item">
          <svg class="contact__icon" viewBox="0 0 18 18" fill="none" stroke="#84678f" stroke-width="1.6">
            <rect x="2" y="4" width="14" height="10" rx="1.5"/>
            <polyline points="2.5,4.8 9,10 15.5,4.8"/>
          </svg>
          wrenhalloway@example.com
        </li>
        <li class="contact__item">
          <svg class="contact__icon" viewBox="0 0 18 18" fill="none" stroke="#84678f" stroke-width="1.6">
            <rect x="3" y="3" width="12" height="12" rx="2"/>
          </svg>
          wrenhalloway
        </li>
      </ul>
    </div>

    <div class="services">WEDDINGS • SPECIAL EVENTS • FLORAL CUSTOMERS</div>
  </section>

  <section class="card card--back">
    <div class="side-floral side-floral--left" role="img" aria-label="Silver line-drawn flowers along the left edge"></div>
    <div class="side-floral side-floral--right" role="img" aria-label="Silver line-drawn flowers along the right edge"></div>

    <div class="brand">
      <span class="brand__mark"></span>
      <div class="brand__name">Wren Halloway</div>
      <div class="brand__tagline">DECORATING &amp; FLORALS.</div>
    </div>
  </section>

</div>
</body>
</html>
```